Business card for Mortgage broker business

I have already had the logo designed and am needing a great looking business card. My business focus is on servicing clients who may not be able to obtain finance through traditional lenders due to bad credit, short term employment or they just don't fit the banks profile. It needs to be professional, trust worthy but also have a caring fell about it.
I have provided files showing the green and black logo, the white logo(on white background so the file looks blank) and also a file with the white logo with a background of leaves that was made up which will probably be used for a website header.

Industry/Entity Type

Finance

Contact Information for Business Card

Marcus Dalby
Managing Director, Accredited Finance Broker(AFB)
Po Box 817, Briarwood VIC 3915
marcus@kestrelfunding.com.au
www.kestrelfunding.com.au
0438 216 507

Requirements
Nice to have
• I have added a picture of myself as I would like to see some designs with the pic in it, but I'm not sure if I want it on there with the logo's or just the logo's

```html
<!DOCTYPE html>
<html lang="en">
<head>
<meta charset="utf-8">
<title>Kestrel Funding – Business Card</title>
<link href="https://fonts.googleapis.com/css2?family=Tinos:ital,wght@0,400;0,700;1,400&display=swap" rel="stylesheet">
<style>
  :root {
    --bg: #5a3a2a;
    --card: #13231e;
    --panel: #f1f1f1;
    --brand: #1d7a40;
    --name: #9aa39f;
    --text: #e6e9e7;
    --muted: #8e9894;
  }
  html, body {
    margin: 0;
    width: 1200px;
    height: 864px;
    overflow: hidden;
    background: var(--bg);
    font-family: "Tinos", "Times New Roman", serif;
  }
  .stage {
    position: relative;
    width: 1200px;
    height: 864px;
  }
  .card {
    position: absolute;
    top: 267px;
    width: 540px;
    height: 330px;
    background: var(--card);
    box-shadow: 0 10px 30px rgba(0,0,0,.35);
    overflow: hidden;
  }
  .card--back { left: 40px; }
  .card--front { left: 620px; }

  .back-brand {
    position: absolute;
    inset: 0;
    display: flex;
    align-items: center;
    justify-content: center;
  }
  .back-brand__name {
    color: var(--brand);
    font-size: 48px;
    font-weight: 700;
    letter-spacing: 1px;
  }

  .tab {
    position: absolute;
    left: 205px;
    top: 0;
    width: 90px;
    height: 24px;
    background: var(--panel);
  }
  .portrait {
    position: absolute;
    left: 190px;
    top: 36px;
    width: 122px;
    height: 142px;
    background: linear-gradient(160deg, #ffffff 0%, #e9e4e0 45%, #6b5446 75%, #262a36 100%);
  }
  .logo-band {
    position: absolute;
    left: 330px;
    top: 52px;
    right: 0;
    height: 126px;
    background: var(--panel);
    display: flex;
    align-items: center;
    justify-content: center;
  }
  .logo-band__name {
    color: var(--brand);
    font-size: 26px;
    font-weight: 700;
  }
  .identity {
    position: absolute;
    left: 40px;
    top: 200px;
  }
  .identity__name {
    margin: 0 0 6px;
    color: var(--name);
    font-size: 24px;
    font-weight: 400;
    letter-spacing: 1px;
    text-transform: uppercase;
  }
  .identity__role {
    margin: 0;
    color: var(--text);
    font-size: 15px;
    font-style: italic;
    line-height: 1.35;
  }
  .contact {
    position: absolute;
    left: 318px;
    top: 200px;
    right: 14px;
    margin: 0;
    color: var(--muted);
    font-size: 13px;
    line-height: 1.55;
    white-space: nowrap;
  }
  .contact__label {
    color: var(--text);
    font-weight: 700;
    font-style: italic;
  }
</style>
</head>
<body>
<main class="stage">
  <section class="card card--back" aria-label="Card back">
    <div class="back-brand">
      <span class="back-brand__name">Kestrel Funding</span>
    </div>
  </section>

  <section class="card card--front" aria-label="Card front">
    <div class="tab"></div>
    <div class="portrait" role="img" aria-label="Portrait photo of Marcus Dalby"></div>
    <div class="logo-band">
      <span class="logo-band__name">Kestrel Funding</span>
    </div>
    <div class="identity">
      <h1 class="identity__name">Marcus Dalby</h1>
      <p class="identity__role">Managing Director<br>Accredited Finance Broker(AFB)</p>
    </div>
    <p class="contact">
      <span class="contact__label">mail :</span> marcus@kestrelfunding.com.au<br>
      <span class="contact__label">web :</span> www.kestrelfunding.com.au<br>
      Po Box 817, Briarwood VIC 3915
    </p>
  </section>
</main>
</body>
</html>
```